Oil and Gas Letterhead Design Tweak

Simple letterhead information and design tweak.

Please note, we don't want to change the design or logo of the letterhead only the small changes mentioned below.

We need to change the company name up top to "Northvale Petrotek FZCO"

Also, we need to include in the footer the following information. I have attached an image of roughly how we would like to have it displayed in the footer.

Footer Details:

Northvale Petrotek FZCO,
Unit No. 2378, FZCO Trade Hub, level No. 1, K&P 7, Dubai, United Arab Emirates
Northvale Petrotek FZCO is registered as a free zone company under the rules & regulations of FZCO

Target Market(s)

O&G Market

Industry/Entity Type

Oil And Gas

Font styles to use
Sans Serif

Colors

Designer to choose colors to be used in the design.

Requirements
Must have
• Change the company name to Northvale Petrotek FZCO
• Include the footer on the bottom of the first and continuation page
Should not have
• Should not change the design or logo of the letterhead, only the specified changes mentioned above

```html
<!DOCTYPE html>
<html lang="en">
<head>
<meta charset="utf-8">
<title>Northvale Petrotek FZCO – Letterhead</title>
<link rel="stylesheet" href="https://fonts.googleapis.com/css2?family=Montserrat:wght@400;500;600;700&display=swap">
<style>
  :root {
    --backdrop: #eef1f4;
    --paper: #ffffff;
    --brand-blue: #1559a8;
    --brand-red: #e42229;
    --ink: #23262b;
    --ink-soft: #4a4e55;
  }
  * { box-sizing: border-box; margin: 0; padding: 0; }
  html, body {
    width: 1200px; height: 926px; overflow: hidden;
    background: var(--backdrop);
    font-family: "Montserrat", sans-serif;
  }
  .canvas { position: relative; width: 1200px; height: 926px; }
  .sheet {
    position: absolute; top: 178px;
    width: 404px; height: 571px;
    background: var(--paper);
    box-shadow: 0 1px 3px rgba(0,0,0,0.12);
    overflow: hidden;
  }
  .sheet--first { left: 126px; }
  .sheet--continuation { left: 671px; }
  .sheet__bands { position: absolute; inset: 0; width: 404px; height: 571px; }
  .band--blue { fill: var(--brand-blue); }
  .band--red { fill: var(--brand-red); }

  .header-name {
    position: absolute; left: 128px; top: 21px;
    font-size: 11.5px; font-weight: 600; letter-spacing: 0.2px;
    color: var(--ink); white-space: nowrap;
  }

  .footer { position: absolute; left: 15px; top: 529px; color: var(--ink-soft); }
  .footer__name {
    font-size: 5px; font-weight: 700; color: var(--ink);
    text-transform: uppercase; letter-spacing: 0.1px;
  }
  .footer__address {
    display: flex; align-items: center; margin-top: 5px;
    font-size: 4.6px; white-space: nowrap;
  }
  .footer__address span + span {
    border-left: 0.8px solid var(--ink);
    margin-left: 9px; padding-left: 8px;
  }
  .footer__legal { margin-top: 6px; font-size: 4.5px; white-space: nowrap; }

  .footer__brand {
    position: absolute; left: 300px; top: 528px; width: 60px;
    text-align: center;
    font-size: 4.6px; font-weight: 700; line-height: 1.2;
    color: var(--ink); text-transform: uppercase;
  }
</style>
</head>
<body>
<main class="canvas">

  <section class="sheet sheet--first" aria-label="First page letterhead">
    <svg class="sheet__bands" viewBox="0 0 404 571" aria-hidden="true">
      <polygon class="band--blue" points="0,0 93,0 89,7 0,7"/>
      <polygon class="band--red" points="125,0 404,0 404,7 129,7"/>
      <polygon class="band--blue" points="298,564 313,564 309,571 294,571"/>
      <polygon class="band--red" points="318,564 334,564 337,571 313,571"/>
    </svg>
    <div class="header-name">NORTHVALE PETROTEK FZCO</div>
  </section>

  <section class="sheet sheet--continuation" aria-label="Continuation page letterhead">
    <svg class="sheet__bands" viewBox="0 0 404 571" aria-hidden="true">
      <polygon class="band--blue" points="297,0 329,0 324,12 302,12"/>
      <polygon class="band--red" points="334,0 358,0 353,12 329,12"/>
      <polygon class="band--blue" points="0,564 300,564 297,571 0,571"/>
      <polygon class="band--red" points="354,559 404,559 404,571 360,571"/>
    </svg>

    <div class="footer">
      <div class="footer__name">Northvale Petrotek FZCO</div>
      <div class="footer__address">
        <span>Unit No. 2378</span>
        <span>FZCO Trade Hub</span>
        <span>level No. 1, K&amp;P 7</span>
        <span>Dubai</span>
        <span>United Arab Emirates</span>
      </div>
      <div class="footer__legal">Northvale Petrotek FZCO is registered as a free zone company under the rules &amp; regulations of FZCO</div>
    </div>

    <div class="footer__brand">Northvale<br>Petrotek FZCO</div>
  </section>

</main>
</body>
</html>
```